Automotive Locksmiith company needs a website design and mobile website

We need a website design and a mobile design for an automotive locksmith company called Cedarline Autoworks LLC.We are based in the center of the Dallas-Fort Worth Metroplex. We have a website that was directed more towards the towing services we also offer. We would like to have it more towards our locksmith products. Our main services include:
Auto keys duplication
Cutting of new car keys
Car Lockouts
Laser key replacement
Cutting keys by code
Broken key extractions
Production of transponder keys
Key fob programming
Door lock repairs
Ignition repairs/replacement
We work on 95% of the automotive market that includes Vorra, Belvo, KTZ, Merrowind, Tanquelle, Polgrave, Brunt, QR, Solvane, Pirel, Zoravelo, Uto, Harwick, Quorel, Telvar, Ostravin, Fendale, Pavo, Rulko Kelvarona , Brisel, Varuno, Drexmotor, Tesko.
We are one of the most affordable services in the DFW area . Our prices for transponder copies start at $35 per key. We provide services for high-end vehicles also as KTZ and Ostravin. We can program the new proximity keys for Telvar Vehicles 2013-up. We also work on the new Pell Vehicles 20-13 and up including the Pell Caravel head remote key.
We would like to have a similar style to the website we already have with the option to schedule an appointment on the mobile website. This mobile application will deliver an email when a new customer is requiring the service. It will ask for Year, Make, Model , Service to be performed( Key copy, Lockout, Lost Key, Change Ignition lock, change door lock, Other services.) Description of the service to be performed, Address, Select time of service.
Our current website is cedarlineautoworks.example

Reason: Need pictures of webpages inside design (about us , location etc) and mobile pictures( how website looks in zelPad / norvix)

Automotive

• check word attachment

```html
<!DOCTYPE html>
<html lang="en">
<head>
<meta charset="utf-8">
<title>Cedarline Autoworks LLC – Services</title>
<link rel="stylesheet" href="https://fonts.googleapis.com/css2?family=Ubuntu:wght@400;500;700&family=Open+Sans:wght@800&display=swap">
<style>
:root{
  --white:#ffffff;
  --ink:#1d2a33;
  --brand:#4d6e7c;
  --brand-dark:#1f3c5a;
  --nav:#5d717d;
  --nav-dark:#4c606c;
  --hero:#1a8cb0;
  --hero-deep:#11728f;
  --cyan:#1ab4e2;
  --text-light:#e8f7fd;
  --footer:#2b2f37;
  --footer-text:#d9dde2;
  --bar:#1d9bc7;
  --search:#dfe6ea;
}
*{box-sizing:border-box;margin:0;padding:0}
html,body{width:726px;height:1200px;overflow:hidden}
body{font-family:"Ubuntu",sans-serif;background:var(--white);position:relative;color:var(--ink)}
.header{position:absolute;left:0;top:0;width:726px;height:93px;background:var(--white)}
.brand{position:absolute;left:67px;top:55px;display:flex;align-items:center;gap:7px}
.brand-mark{width:12px;height:12px;background:var(--brand-dark)}
.brand-name{font-size:21px;font-weight:500;color:var(--brand);letter-spacing:-.3px}
.top-contact{position:absolute;top:17px;left:435px;display:flex;gap:12px;font-size:9.5px;color:#55616a;align-items:center}
.top-contact span{display:flex;align-items:center;gap:5px}
.search{position:absolute;left:481px;top:55px;width:177px;height:23px;display:flex}
.search-field{flex:1;background:var(--search);font-size:11px;color:#9aa8b0;padding:5px 9px}
.search-btn{width:29px;background:var(--nav);display:flex;align-items:center;justify-content:center}
.nav{position:absolute;left:0;top:93px;width:726px;height:39px;background:linear-gradient(var(--nav),var(--nav-dark))}
.nav a{position:absolute;top:11px;font-size:14.5px;color:#141c22;text-decoration:none;font-weight:500}
.nav a.active{color:var(--white)}
.hero{position:absolute;left:0;top:132px;width:726px;height:250px;background:linear-gradient(160deg,var(--hero) 0%,var(--hero-deep) 100%);overflow:hidden}
.hero-title{position:absolute;left:96px;top:96px;font-family:"Open Sans",sans-serif;font-weight:800;font-size:46px;color:var(--white);letter-spacing:.5px}
.hero-diagram{position:absolute;left:372px;top:22px;width:266px;height:205px;border-radius:50%;background:radial-gradient(ellipse at center,rgba(26,180,226,.55) 0%,rgba(23,113,141,.55) 45%,rgba(17,114,143,0) 72%)}
.services{position:absolute;left:0;top:382px;width:726px;height:620px;background:var(--cyan)}
.service{position:absolute;width:300px;height:180px}
.service-icon{position:absolute;left:0;top:0;width:90px;height:90px;border-radius:50%;background:var(--white);box-shadow:0 6px 10px rgba(0,0,0,.15);display:flex;align-items:center;justify-content:center}
.service-title{position:absolute;left:104px;top:6px;font-size:15px;font-weight:700;color:var(--white);white-space:nowrap}
.service-text{position:absolute;left:105px;top:32px;width:186px;font-size:9.1px;line-height:12px;color:var(--text-light)}
.footer{position:absolute;left:0;top:1002px;width:726px;height:166px;background:var(--footer);color:var(--footer-text)}
.footer h3{position:absolute;font-size:12.5px;font-weight:500;color:var(--white)}
.social{position:absolute;left:73px;top:41px;display:flex;gap:19px}
.social span{width:21px;height:21px;border:1.5px solid var(--white);border-radius:50%}
.links{position:absolute;left:75px;top:93px;list-style:none;font-size:9.5px;line-height:20px}
.contact-line{position:absolute;left:277px;display:flex;gap:10px;font-size:9.5px;letter-spacing:.8px;line-height:17px}
.map{position:absolute;left:427px;top:40px;width:234px;height:74px;background:linear-gradient(135deg,#e6e2d6,#cfd8d6 60%,#b9cfdc);border:2px solid var(--white)}
.bottom-bar{position:absolute;left:0;top:1168px;width:726px;height:32px;background:var(--bar);color:var(--white);font-size:12px;text-align:center;line-height:32px}
</style>
</head>
<body>
<header class="header">
  <div class="brand"><span class="brand-mark"></span><span class="brand-name">CedarlineAutoworks LLC</span></div>
  <div class="top-contact">
    <span><svg width="13" height="9" viewBox="0 0 13 9"><rect x=".5" y=".5" width="12" height="8" fill="none" stroke="#55616a"/><path d="M.5 .5l6 4.5 6-4.5" fill="none" stroke="#55616a"/></svg>cedarlineautoworks.example</span>
    <span><svg width="13" height="9" viewBox="0 0 13 9"><path d="M1 3q5.5-4 11 0l-2 1.5-1-1.5h-5l-1 1.5zM3.5 4h6l1.5 4.5h-9z" fill="#55616a"/></svg>+100-555-0142</span>
  </div>
  <div class="search"><div class="search-field">search</div><div class="search-btn"><svg width="12" height="12" viewBox="0 0 12 12"><circle cx="5" cy="5" r="3.6" fill="none" stroke="#fff" stroke-width="1.5"/><path d="M7.6 7.6l3.4 3.4" stroke="#fff" stroke-width="1.6"/></svg></div></div>
</header>

<nav class="nav">
  <a style="left:78px">Home</a>
  <a style="left:155px">About Us</a>
  <a class="active" style="left:252px">Services</a>
  <a style="left:343px">Locksmith services</a>
  <a style="left:504px">Price list</a>
  <a style="left:596px">Contact</a>
</nav>

<section class="hero">
  <h1 class="hero-title">SERVICES</h1>
  <div class="hero-diagram" role="img" aria-label="Illustration of locksmith services around a technician: auto keys duplication, cutting of new car keys, car lockouts, laser key replacement, key fob programming, production of transponder keys, broken key extractions, cutting keys by code"></div>
</section>

<main class="services">
  <article class="service" style="left:67px;top:31px">
    <div class="service-icon"><svg width="60" height="40" viewBox="0 0 60 40"><path d="M4 18h20l4-8h10v14h16v8H4z" fill="#1d2a33"/><path d="M38 24l16-18" stroke="#1d2a33" stroke-width="3"/><circle cx="14" cy="32" r="5" fill="#1d2a33" stroke="#fff" stroke-width="2"/><circle cx="44" cy="32" r="5" fill="#1d2a33" stroke="#fff" stroke-width="2"/></svg></div>
    <h2 class="service-title">Towing Services</h2>
    <p class="service-text">Lorem Ipsum is simply dummy text of the printing and typesetting industry. Lorem Ipsum has been the industry's standard dummy text ever since the 1500s, when an unknown printer took a galley of type and scrambled it to make a type specimen book. It has survived not only five centuries, but also the leap into electronic typesetting, remaining essentially unchanged. It was popularised in the 1960s with the release of Letraset sheets containing</p>
  </article>
  <article class="service" style="left:363px;top:33px">
    <div class="service-icon"><svg width="44" height="50" viewBox="0 0 44 50"><rect x="4" y="2" width="36" height="40" rx="3" fill="#1d2a33"/><rect x="9" y="8" width="26" height="14" fill="#fff"/><rect x="9" y="26" width="26" height="2" fill="#fff"/><rect x="9" y="31" width="26" height="2" fill="#fff"/><rect x="7" y="42" width="7" height="6" fill="#1d2a33"/><rect x="30" y="42" width="7" height="6" fill="#1d2a33"/></svg></div>
    <h2 class="service-title" style="left:102px;top:3px">Vehicle Transport</h2>
    <p class="service-text" style="left:103px;top:29px">Lorem Ipsum is simply dummy text of the printing and typesetting industry. Lorem Ipsum has been the industry's standard dummy text ever since the 1500s, when an unknown printer took a galley of type and scrambled it to make a type specimen book. It has survived not only five centuries, but also the leap into electronic typesetting, remaining essentially unchanged. It was popularised in the 1960s with the release of Letraset sheets containing</p>
  </article>
  <article class="service" style="left:67px;top:222px">
    <div class="service-icon"><svg width="44" height="52" viewBox="0 0 44 52"><circle cx="10" cy="9" r="6" fill="#1d2a33"/><path d="M15 7h22v4h-4v3h-4v-3H15z" fill="#1d2a33"/><path d="M6 30l5-10h22l5 10v16h-6v-4H12v4H6z" fill="#1d2a33"/><rect x="14" y="23" width="16" height="6" fill="#fff"/><circle cx="13" cy="35" r="2.5" fill="#fff"/><circle cx="31" cy="35" r="2.5" fill="#fff"/></svg></div>
    <h2 class="service-title" style="left:102px;top:2px">Locksmith Service</h2>
    <p class="service-text" style="left:102px;top:28px">Lorem Ipsum is simply dummy text of the printing and typesetting industry. Lorem Ipsum has been the industry's standard dummy text ever since the 1500s, when an unknown printer took a galley of type and scrambled it to make a type specimen book. It has survived not only five centuries, but also the leap into electronic typesetting, remaining essentially unchanged. It was popularised in the 1960s with the release of Letraset sheets containing</p>
  </article>
  <article class="service" style="left:363px;top:222px">
    <div class="service-icon"><svg width="56" height="44" viewBox="0 0 56 44"><path d="M4 18l6-8h26v26H4z" fill="#1d2a33"/><rect x="9" y="13" width="10" height="7" fill="#fff"/><circle cx="12" cy="36" r="5" fill="#1d2a33" stroke="#fff" stroke-width="2"/><circle cx="30" cy="36" r="5" fill="#1d2a33" stroke="#fff" stroke-width="2"/><circle cx="41" cy="14" r="11" fill="#fff" stroke="#1d2a33" stroke-width="3"/><path d="M41 8v6h5" fill="none" stroke="#1d2a33" stroke-width="2"/></svg></div>
    <h2 class="service-title" style="left:105px;top:1px">Product Delivery</h2>
    <p class="service-text" style="left:105px;top:27px">Lorem Ipsum is simply dummy text of the printing and typesetting industry. Lorem Ipsum has been the industry's standard dummy text ever since the 1500s, when an unknown printer took a galley of type and scrambled it to make a type specimen book. It has survived not only five centuries, but also the leap into electronic typesetting, remaining essentially unchanged. It was popularised in the 1960s with the release of Letraset sheets containing</p>
  </article>
  <article class="service" style="left:67px;top:416px">
    <div class="service-icon"><svg width="52" height="46" viewBox="0 0 52 46"><path d="M8 16h30v26H8z" fill="none" stroke="#1d2a33" stroke-width="5"/><path d="M4 12l12-8 14 6 16-4v12H4z" fill="#1d2a33"/></svg></div>
    <h2 class="service-title" style="left:103px;top:4px">Free Storage</h2>
    <p class="service-text" style="left:103px;top:30px">Lorem Ipsum is simply dummy text of the printing and typesetting industry. Lorem Ipsum has been the industry's standard dummy text ever since the 1500s, when an unknown printer took a galley of type and scrambled it to make a type specimen book. It has survived not only five centuries, but also the leap into electronic typesetting, remaining essentially unchanged. It was popularised in the 1960s with the release of Letraset sheets containing</p>
  </article>
  <article class="service" style="left:363px;top:414px">
    <div class="service-icon"><svg width="50" height="50" viewBox="0 0 50 50"><path d="M6 14c0-4 4-7 7-6l4 8-4 4c3 7 8 12 15 15l4-4 8 4c1 3-2 7-6 7C19 42 6 29 6 14z" fill="#1d2a33"/><path d="M36 2a12 10 0 1 1-8 18l-5 3 2-6A12 10 0 0 1 36 2z" fill="#1d2a33"/><circle cx="31" cy="12" r="1.8" fill="#fff"/><circle cx="36" cy="12" r="1.8" fill="#fff"/><circle cx="41" cy="12" r="1.8" fill="#fff"/></svg></div>
    <h2 class="service-title" style="left:105px;top:5px">Customer Care</h2>
    <p class="service-text" style="left:105px;top:31px">Lorem Ipsum is simply dummy text of the printing and typesetting industry. Lorem Ipsum has been the industry's standard dummy text ever since the 1500s, when an unknown printer took a galley of type and scrambled it to make a type specimen book. It has survived not only five centuries, but also the leap into electronic typesetting, remaining essentially unchanged. It was popularised in the 1960s with the release of Letraset sheets containing</p>
  </article>
</main>

<footer class="footer">
  <h3 style="left:74px;top:16px">Follow Us</h3>
  <div class="social"><span></span><span></span><span></span><span></span></div>
  <h3 style="left:74px;top:74px">Important Links</h3>
  <ul class="links"><li>Our Services</li><li>Locksmith services</li><li>Price list</li></ul>
  <h3 style="left:274px;top:16px">Contact Us</h3>
  <div class="contact-line" style="top:48px"><svg width="8" height="11" viewBox="0 0 8 11"><path d="M4 0a4 4 0 0 1 4 4c0 3-4 7-4 7S0 7 0 4a4 4 0 0 1 4-4z" fill="#fff"/><circle cx="4" cy="4" r="1.5" fill="#2b2f37"/></svg><span>4120 HALBROOK AVE<br>DALLAS, TX 75209</span></div>
  <div class="contact-line" style="top:101px"><svg width="10" height="10" viewBox="0 0 10 10"><path d="M1 2c0-1 1-2 2-1l1 2-1 1c1 2 2 3 3 3l1-1 2 1c1 1 0 2-1 2C4 9 1 6 1 2z" fill="#fff"/></svg><span>+888-555-0193</span></div>
  <div class="contact-line" style="top:132px"><svg width="11" height="10" viewBox="0 0 11 10"><path d="M1 4l4.5-3 4.5 3v5H1z" fill="none" stroke="#fff"/><path d="M1 4l4.5 3 4.5-3" fill="none" stroke="#fff"/></svg><span>contact@cedarlineautoworks.example</span></div>
  <div class="map" role="img" aria-label="Map showing the workshop location"></div>
</footer>

<div class="bottom-bar">All Rights Reserved@ 2014 contact@cedarlineautoworks.example</div>
</body>
</html>
```